People Analytics Company needs Web Design and CSS

We need a refreshed design for a People Analytics company called VOMTA Systems Inc. We have developed an online survey tool that our immediate need is to make it look snazzier for upcoming pilots with prospective companies. Dark Blue and Orange are the colors we like to use but the survey should be "neutral" - we don't want to influence any responses based on colors.

Target Market(s)

Enterprise Users

Industry/Entity Type

It Company

Coding

Coded - Design and coding required

Number of Pages Required

3 page

Font styles to use
Sans Serif

Colors
0556a4
f37122

Requirements
Must have
• User friendly way of responding to survey questions that is suitable for a tablet (fat fingers). Drag and Drop is also very hard on tablet.
• Neutral look and feel to reduce any potential respondent bias.
• Colors consistent with brand colors attached in document.
• Minimal scrolling is best.
Should not have
• Too many colors.

```html
<!DOCTYPE html>
<html lang="en">
<head>
<meta charset="utf-8">
<title>VOMTA Systems Inc. – Survey</title>
<link href="https://fonts.googleapis.com/css2?family=Roboto:wght@400;500;700&display=swap" rel="stylesheet">
<style>
  :root{
    --brand-blue:#0556a4;
    --brand-blue-dark:#063f7c;
    --brand-orange:#f37122;
    --orange-top:#f18a26;
    --orange-bottom:#e2690b;
    --navy:#0c1a45;
    --page:#f7f7f7;
    --rule:#dedede;
    --text:#7a7a7a;
    --title:#6b6b6b;
    --nav:#777;
    --footer:#333;
  }
  *{box-sizing:border-box;margin:0;padding:0}
  html,body{width:1200px;height:999px;overflow:hidden}
  body{position:relative;background:var(--page);font-family:Roboto,Arial,sans-serif;color:var(--text)}

  .site-header{position:absolute;left:0;top:0;width:1200px;height:123px;background:#fff;border-top:3px solid var(--brand-orange);box-shadow:0 1px 3px rgba(0,0,0,.05)}
  .brand{position:absolute;left:99px;top:21px;display:flex;align-items:center;gap:8px;color:var(--navy);font-weight:700}
  .brand-mark{width:82px;height:80px;background:var(--navy);border-radius:6px}
  .brand-name{line-height:1}
  .brand-name .big{display:block;font-size:48px;letter-spacing:-1px}
  .brand-name .small{display:block;font-size:15px;margin-top:4px}

  .main-nav{position:absolute;top:62px;font-size:14px;color:var(--nav);text-transform:uppercase}
  .main-nav a{position:absolute;white-space:nowrap;color:inherit;text-decoration:none}
  .btn{position:absolute;display:flex;align-items:center;justify-content:center;color:#fff;font-weight:500;text-decoration:none}
  .btn-signin{left:865px;top:50px;width:97px;height:38px;background:linear-gradient(var(--orange-top),var(--orange-bottom));font-size:16px;border-radius:2px}
  .btn-start{left:969px;top:50px;width:132px;height:38px;background:linear-gradient(#0a62b5,var(--brand-blue-dark));font-size:16px;border-radius:2px}

  .survey{position:absolute;left:99px;top:153px;width:1001px;border-collapse:collapse;table-layout:fixed}
  .survey th{height:59px;background:linear-gradient(var(--orange-top),var(--orange-bottom));color:#fff;text-align:left;font-weight:400;padding:0 0 0 16px;border-left:1px solid rgba(255,255,255,.35);vertical-align:middle}
  .survey th:first-child{border-left:0}
  .survey th span{display:block;font-size:13px;line-height:16px}
  .survey th strong{display:block;font-size:16.5px;font-weight:500;line-height:22px}
  .survey td{height:83px;border-left:1px solid var(--rule);border-top:1px solid #e8e8e8;background:linear-gradient(#fff,#f2f2f2);vertical-align:middle}
  .survey td:first-child{border-left:0}
  .survey tr:last-child td{border-bottom:1px solid var(--rule)}
  .survey td:last-child{border-right:1px solid #e8e8e8}
  .statement{padding:0 8px 0 10px;font-size:11.4px;line-height:19px}
  .statement b{font-weight:400;font-size:13px;color:var(--title);text-decoration:underline}
  .choice{text-align:center}
  .radio{display:inline-block;width:15px;height:15px;border-radius:50%;border:1px solid #cfcfcf;background:linear-gradient(#f0f0f0,#fff)}

  .btn-continue{left:963px;top:823px;width:137px;height:41px;background:linear-gradient(#0a62b5,var(--brand-blue-dark));font-size:20px;font-weight:400;gap:8px;border:1px solid #04407c}

  .site-footer{position:absolute;left:0;top:898px;width:1200px;height:101px;background:var(--footer);color:#fff}
  .copyright{position:absolute;left:100px;top:42px;font-size:11px}
  .social{position:absolute;top:36px;left:931px;display:flex;gap:6px}
  .social span{width:29px;height:29px;border-radius:50%;background:#555}
  .page-code{position:absolute;left:1116px;top:83px;font-size:10px}
</style>
</head>
<body>
  <header class="site-header">
    <div class="brand">
      <div class="brand-mark"></div>
      <div class="brand-name"><span class="big">VOMTA</span><span class="small">Systems Inc.</span></div>
    </div>
    <nav class="main-nav">
      <a href="#" style="left:477px">Home</a>
      <a href="#" style="left:580px">Our Philosophy</a>
      <a href="#" style="left:760px">Who We Are</a>
    </nav>
    <a class="btn btn-signin" href="#">SIGN IN</a>
    <a class="btn btn-start" href="#">GET STARTED</a>
  </header>

  <table class="survey">
    <colgroup><col style="width:232px"><col style="width:147px"><col style="width:143px"><col style="width:148px"><col style="width:134px"><col style="width:197px"></colgroup>
    <thead>
      <tr>
        <th></th>
        <th><span>LEFT STATMENT</span><strong>MUCH BETTER</strong></th>
        <th><span>LEFT STATEMENT</span><strong>BETTER</strong></th>
        <th><span>RIGHT STATEMENT</span><strong>BETTER</strong></th>
        <th style="padding-left:12px"><span>RIGHT STATEMENT</span><strong>MUCH BETTER</strong></th>
        <th></th>
      </tr>
    </thead>
    <tbody>
      <tr>
        <td class="statement"><b>THE COACH-</b>We continuously track and monitor the market on what people value effectiveness in different situations.</td>
        <td class="choice"><span class="radio"></span></td><td class="choice"><span class="radio"></span></td><td class="choice"><span class="radio"></span></td><td class="choice"><span class="radio"></span></td>
        <td class="statement"><b>SINK OR SWIM-</b>We continuously track and monitor the market on in different situations.</td>
      </tr>
      <tr>
        <td class="statement"><b>INSPIRATIONAL -</b>We continuously track monitor the market on what people value effectiveness in different situations.</td>
        <td class="choice"><span class="radio"></span></td><td class="choice"><span class="radio"></span></td><td class="choice"><span class="radio"></span></td><td class="choice"><span class="radio"></span></td>
        <td class="statement"><b>FUNCTIONAL -</b>We continuously track and monitor the market on in different situations.</td>
      </tr>
      <tr>
        <td class="statement"><b>DEMOCRATIC-</b>We continuously track &amp; monitor the market on what people value effectiveness in different situations.</td>
        <td class="choice"><span class="radio"></span></td><td class="choice"><span class="radio"></span></td><td class="choice"><span class="radio"></span></td><td class="choice"><span class="radio"></span></td>
        <td class="statement"><b>COMMANDING-</b>We continuously track and monitor the market on in different situations.</td>
      </tr>
      <tr>
        <td class="statement"><b>HANDS ON-</b>We continuously track and monitor the market on what people value effectiveness in different situations.</td>
        <td class="choice"><span class="radio"></span></td><td class="choice"><span class="radio"></span></td><td class="choice"><span class="radio"></span></td><td class="choice"><span class="radio"></span></td>
        <td class="statement"><b>HANDS OFF-</b>We continuously track and monitor the market on in different situations.</td>
      </tr>
      <tr>
        <td class="statement"><b>BY THE BOOK-</b>We continuously track &amp; monitor the market on what people value effectiveness in different situations.</td>
        <td class="choice"><span class="radio"></span></td><td class="choice"><span class="radio"></span></td><td class="choice"><span class="radio"></span></td><td class="choice"><span class="radio"></span></td>
        <td class="statement"><b>BURN THE BOOK-</b>We continsly track and monitor the market on in different situations.</td>
      </tr>
      <tr>
        <td class="statement"><b>MASTER MANAGER-</b>We continuously monitor the market on what people value effectiveness in different situations.</td>
        <td class="choice"><span class="radio"></span></td><td class="choice"><span class="radio"></span></td><td class="choice"><span class="radio"></span></td><td class="choice"><span class="radio"></span></td>
        <td class="statement"><b>IN THETRENCHES-</b>We continly track and monitor the market on in different situations.</td>
      </tr>
      <tr>
        <td class="statement"><b>EVEN KEEL-</b>We continuously track and monitor the market on what people value effectiveness in different situations.</td>
        <td class="choice"><span class="radio"></span></td><td class="choice"><span class="radio"></span></td><td class="choice"><span class="radio"></span></td><td class="choice"><span class="radio"></span></td>
        <td class="statement"><b>HIGHS AND LOWS-</b>We continsly track and monitor the market on in different situations.</td>
      </tr>
    </tbody>
  </table>

  <a class="btn btn-continue" href="#">Countinue
    <svg width="14" height="14" viewBox="0 0 14 14" fill="none" stroke="#fff" stroke-width="2"><path d="M2 2l5 5-5 5M7 2l5 5-5 5"/></svg>
  </a>

  <footer class="site-footer">
    <p class="copyright">© Copy Right 2105 VOMTA.All copyrights Reserved.</p>
    <div class="social" aria-label="Social links">
      <span></span><span></span><span></span><span></span><span></span>
    </div>
    <span class="page-code">C2</span>
  </footer>
</body>
</html>
```